Design graphics and Print for a line of Herb Seeds- Envelope Design

We need a set of herb seed envelopes designed for a new seed line we are launching.
The design will be both front and back

Envelope will be a colored ( green) ) envelope with white text
or a white or cream envelope in all black /and images text. Or can add some colors to the white envelope.

I have attached the die-cut of the seed envelope.
I have attached some images of envelopes I like. Please do not copy, these are just to give you an idea of what I like.

Please feel free to reach out to me if you have any questions.

Thank you

Target Market(s)

The design needs to classic that can translate to 3 different audiences. 1. young parents 2. hip, young single millennial 3. kids

Industry/Entity Type

Ecommerce

Font styles to use
Serif

Requirements
Must have
• Please use the herb - Parsley for the design
Icon, Text or both.

Front side must have:
1.either herb Icon or work Parsley or both- this will be the main attraction
2. company name- Tall Meadow Pantry
3. can use design elements
4. can use my logo on from or back or not at all. I

Backside must have:
1. social media tags
FB, Instagram and Pinterest ( use icons) @tallmeadowpantry

my website: www.tallmeadowpantry.example
this can be on from or back of the envelope.
Should not have
• please stay away from "county" flowery, old fashioned style designs

```html
<!DOCTYPE html>
<html lang="en">
<head>
<meta charset="utf-8">
<title>Tall Meadow Pantry – Parsley Seed Envelopes</title>
<link rel="stylesheet" href="https://fonts.googleapis.com/css2?family=Lobster&family=Courgette&family=Open+Sans:wght@400;600&display=swap">
<style>
  :root {
    --canvas: #ffffff;
    --cream: #e6dccb;
    --forest: #3d5245;
    --fold-on-cream: #6f7d72;
    --fold-on-forest: #c3ccc5;
    --white: #ffffff;
  }
  html, body {
    margin: 0;
    padding: 0;
    width: 1200px;
    height: 1200px;
    overflow: hidden;
    background: var(--canvas);
  }
  .sheet { display: block; width: 1200px; height: 1200px; }

  .envelope--cream .die-cut { fill: var(--cream); }
  .envelope--cream .fold-line { stroke: var(--fold-on-cream); }
  .envelope--cream .ink { fill: var(--forest); }
  .envelope--cream .ink-stroke { stroke: var(--forest); }

  .envelope--forest .die-cut { fill: var(--forest); }
  .envelope--forest .fold-line { stroke: var(--fold-on-forest); }
  .envelope--forest .ink { fill: var(--white); }
  .envelope--forest .ink-stroke { stroke: var(--white); }

  .fold-line { stroke-width: 1; fill: none; }
  .ink-stroke { fill: none; stroke-width: 1.5; }

  .herb-title { font-family: "Lobster", cursive; font-size: 70px; }
  .brand-line { font-family: "Courgette", cursive; font-size: 21px; }
  .seal-name { font-family: "Open Sans", sans-serif; font-size: 10px; font-weight: 600; letter-spacing: 0.5px; }
  .web-address, .social-handle { font-family: "Open Sans", sans-serif; font-size: 10px; }
</style>
</head>
<body>
<svg class="sheet" viewBox="0 0 1200 1200" xmlns="http://www.w3.org/2000/svg">

  <!-- Cream envelope -->
  <g class="envelope envelope--cream">
    <path class="die-cut back-flap" d="M576,143 L318,143 Q296,143 296,165 L296,531 Q296,553 318,553 L576,553 Z"/>
    <path class="die-cut front-panel" d="M597,123 L597,100 Q597,88 609,88 L875,88 Q887,88 887,100 L887,123 L909,145 L909,553 L887,575 L887,598 Q887,610 875,610 L609,610 Q597,610 597,598 L597,575 L576,553 L576,143 Z"/>
    <path class="die-cut side-flap" d="M909,145 L933,145 Q945,145 945,157 L945,541 Q945,553 933,553 L909,553 Z"/>
    <line class="fold-line" x1="597" y1="123" x2="887" y2="123"/>
    <line class="fold-line" x1="597" y1="575" x2="887" y2="575"/>
    <line class="fold-line" x1="576" y1="143" x2="576" y2="553"/>
    <line class="fold-line" x1="909" y1="145" x2="909" y2="553"/>

    <g class="back-info">
      <circle class="ink-stroke" cx="461" cy="327" r="24"/>
      <text class="seal-name ink" x="461" y="368" text-anchor="middle">Tall Meadow Pantry</text>
      <text class="web-address ink" x="461" y="391" text-anchor="middle">www.tallmeadowpantry.example</text>
      <text class="social-handle ink" x="461" y="491" text-anchor="middle">@tallmeadowpantry</text>
    </g>

    <g class="front-info">
      <text class="herb-title ink" x="745" y="235" text-anchor="middle">Parsley</text>
      <rect class="ink" x="625" y="285" width="210" height="215" rx="6" opacity="0.9" role="img" aria-label="Parsley sprig illustration"/>
      <text class="brand-line ink" x="743" y="537" text-anchor="middle">Tall Meadow Pantry</text>
    </g>
  </g>

  <!-- Forest green envelope -->
  <g class="envelope envelope--forest" transform="translate(0,541)">
    <path class="die-cut back-flap" d="M576,143 L318,143 Q296,143 296,165 L296,531 Q296,553 318,553 L576,553 Z"/>
    <path class="die-cut front-panel" d="M597,123 L597,100 Q597,88 609,88 L875,88 Q887,88 887,100 L887,123 L909,145 L909,553 L887,575 L887,598 Q887,610 875,610 L609,610 Q597,610 597,598 L597,575 L576,553 L576,143 Z"/>
    <path class="die-cut side-flap" d="M909,145 L933,145 Q945,145 945,157 L945,541 Q945,553 933,553 L909,553 Z"/>
    <line class="fold-line" x1="597" y1="123" x2="887" y2="123"/>
    <line class="fold-line" x1="597" y1="575" x2="887" y2="575"/>
    <line class="fold-line" x1="576" y1="143" x2="576" y2="553"/>
    <line class="fold-line" x1="909" y1="145" x2="909" y2="553"/>

    <g class="back-info">
      <circle class="ink-stroke" cx="461" cy="327" r="24"/>
      <text class="seal-name ink" x="461" y="368" text-anchor="middle">Tall Meadow Pantry</text>
      <text class="web-address ink" x="461" y="391" text-anchor="middle">www.tallmeadowpantry.example</text>
      <text class="social-handle ink" x="461" y="491" text-anchor="middle">@tallmeadowpantry</text>
    </g>

    <g class="front-info">
      <text class="herb-title ink" x="745" y="235" text-anchor="middle">Parsley</text>
      <rect class="ink" x="625" y="285" width="210" height="215" rx="6" opacity="0.9" role="img" aria-label="Parsley sprig illustration"/>
      <text class="brand-line ink" x="743" y="537" text-anchor="middle">Tall Meadow Pantry</text>
    </g>
  </g>
</svg>
</body>
</html>
```